New Architectural Firm Business Cards

New Business card to compliment previous pixel forum logo (attached). Please design a business card that is simple, modern, creative....please do not use "symbols", simply the logo and associated graphics/text. The front should contain name/address/phone/email/web address (with graphics).....back should be 100% graphic design using the logo somehow. Hoping for a two color (black and yellow) design. full bleed design, no borders

Target Market(s)

Commercial Architecture Clients

Industry/Entity Type

Architecture

Contact Information for Business Card

Please design a business card that is simple, modern, creative....please do not use "symbols", simply the logo and associated graphics/text. The front should contain name/address/phone/email/web address (with graphics).....back should be 100% graphic design using the logo somehow

Font styles to use
Sans Serif

Colors
FFF300
FFF600
FEFA6F
FFFEC7
FFFEE8

Requirements
Must have
• Clean, Modern Design
Should not have
• Stock images or "icons"

```html
<!DOCTYPE html>
<html lang="en">
<head>
<meta charset="utf-8">
<title>Business Card – Front and Back</title>
<link rel="stylesheet" href="https://fonts.googleapis.com/css2?family=Noto+Sans:wght@400;800&display=swap">
<style>
  :root {
    --backdrop: #e6e6e6;
    --paper: #ffffff;
    --ink: #000000;
    --accent: #fff300;
    --reverse-ink: #ffffff;
  }
  * { margin: 0; padding: 0; box-sizing: border-box; }
  html, body {
    width: 1054px; height: 1200px; overflow: hidden;
    background: var(--backdrop);
    font-family: "Noto Sans", Verdana, sans-serif;
  }
  .card {
    position: absolute;
    left: 118px;
    width: 819px;
    height: 468px;
    overflow: hidden;
  }
  .card--front { top: 117px; background: var(--paper); color: var(--ink); }
  .card--back  { top: 615px; background: var(--ink); color: var(--reverse-ink); }

  .card__bands { position: absolute; left: 0; top: 0; width: 819px; height: 468px; }

  .holder-name {
    position: absolute; left: 43px; top: 54px;
    font-size: 38px; font-weight: 800; line-height: 1; letter-spacing: 0.2px;
    white-space: nowrap;
  }
  .holder-title {
    position: absolute; left: 43px; top: 99px;
    font-size: 24px; font-weight: 400; line-height: 1;
    white-space: nowrap;
  }
  .contact-list { position: absolute; left: 43px; top: 169px; list-style: none; }
  .contact-item {
    display: flex; align-items: center;
    height: 44px; font-size: 25px; line-height: 1; white-space: nowrap;
  }
  .contact-item__icon { width: 24px; height: 24px; margin-right: 20px; flex: none; }

  .logo-mark {
    position: absolute;
    width: 146px; height: 146px;
    border-radius: 50%;
    display: flex; align-items: center; justify-content: center;
    font-size: 25px; font-weight: 400; white-space: nowrap;
  }
  .logo-mark--front { left: 541px; top: 58px; border: 1.5px solid var(--accent); color: var(--ink); }
  .logo-mark--back  { left: 336px; top: 160px; border: 1.5px solid var(--reverse-ink); color: var(--accent); }

  .back-web {
    position: absolute; left: 111px; top: 400px;
    font-size: 25px; line-height: 1.2; color: var(--reverse-ink); white-space: nowrap;
  }
</style>
</head>
<body>

<section class="card card--front" aria-label="Card front">
  <svg class="card__bands" viewBox="0 0 819 468" aria-hidden="true">
    <polygon points="0,395 453,395 481,438 0,438" fill="var(--accent)"/>
    <polygon points="469,395 819,395 819,438 497,438" fill="var(--ink)"/>
  </svg>

  <h1 class="holder-name">Your Name</h1>
  <p class="holder-title">Your Title</p>

  <ul class="contact-list">
    <li class="contact-item">
      <svg class="contact-item__icon" viewBox="0 0 24 24" aria-hidden="true">
        <path d="M12 1.5a7.5 7.5 0 0 0-7.5 7.5c0 5.3 7.5 13.5 7.5 13.5s7.5-8.2 7.5-13.5A7.5 7.5 0 0 0 12 1.5zm0 10.6a3.1 3.1 0 1 1 0-6.2 3.1 3.1 0 0 1 0 6.2z" fill="var(--accent)"/>
      </svg>
      address
    </li>
    <li class="contact-item">
      <svg class="contact-item__icon" viewBox="0 0 24 24" aria-hidden="true">
        <path d="M6.6 2.5l3 4.3-2 2.2c1.3 2.8 3.6 5.1 6.4 6.4l2.2-2 4.3 3-1.6 3.9C12.7 20.6 3.4 11.3 2.7 4.1z" fill="var(--accent)"/>
      </svg>
      phone
    </li>
    <li class="contact-item">
      <svg class="contact-item__icon" viewBox="0 0 24 24" aria-hidden="true">
        <rect x="1" y="5" width="22" height="14" fill="var(--accent)"/>
        <path d="M1.5 5.5L12 13.5 22.5 5.5M1.5 18.5l8-6.5M22.5 18.5l-8-6.5" stroke="var(--paper)" stroke-width="1.3" fill="none"/>
      </svg>
      e-mail
    </li>
    <li class="contact-item">
      <svg class="contact-item__icon" viewBox="0 0 24 24" aria-hidden="true">
        <g fill="none" stroke="var(--accent)" stroke-width="1.4">
          <circle cx="12" cy="12" r="10"/>
          <ellipse cx="12" cy="12" rx="4.5" ry="10"/>
          <path d="M2 12h20M3.5 7h17M3.5 17h17M12 2v20"/>
        </g>
      </svg>
      web address
    </li>
  </ul>

  <div class="logo-mark logo-mark--front">Logo Here</div>
</section>

<section class="card card--back" aria-label="Card back">
  <svg class="card__bands" viewBox="0 0 819 468" aria-hidden="true">
    <polygon points="0,395 58,395 29,438 0,438" fill="var(--accent)"/>
    <polygon points="350,395 819,395 819,438 307,438" fill="var(--accent)"/>
  </svg>

  <div class="logo-mark logo-mark--back">Logo Here</div>
  <p class="back-web">web address</p>
</section>

</body>
</html>
```